Pepper Meadow Indian Restaurant - Easter Dinner Buffet

Pepper Meadow is an Indian restaurant located in Perth's northern suburbs. We are offering a Special Easter Dinner buffet which runs during all public holidays.

The key points is
1. 35+ Items on the menu
2. Sea Food ,Goat , Lamb, Chicken Varieties
3. Plenty of options for Vegetarians and Vegans,
4. Available during all Easter Holidays (5:30PM-9:30PM)
5. Only available for Dine In
6. Adult Price $34.50; Kids under 12 eat at $21. Kids under 2 Free

Items on the menu are as below.

S.No Category Item
1 Soup Lentil Soup
2 Veg Starters Saudi Aloo (Potato)
3 Veg Starters Veg Pakora
4 Veg Starters Onion Bhaji
5 Veg Starters Veg Samosa
6 Veg Starters Potato Pakora
7 Veg Starters Chutney Aloo (Potato)
8 NV Starters Tandoori Chicken
9 NV Starters Murg (Chicken) Kali Tikka
10 NV Starters Chicken 65
11 NV Starters Lemon Chicken Tikka
12 Veg Curries Potato Curry
13 Veg Curries Mix Vegetable Curry
14 Veg Curries Mushrool Masala
15 Veg Curries Yellow Dal
16 NV Curries Fish Fry
17 NV Curries Goat Curry
18 NV Curries Butter Chicken
19 NV Curries Lamb Rogan Josh
20 NV Curries Goan Fish Curry
21 NV Curries Special Chicken Curry
22 Rice Prawn Biryani
23 Rice Steamed Rice
24 Rice Saffron Rice
25 Breads Chocolate Naan
26 Breads Butter Naan
27 Breads Garlic Nann
28 Sides Raitha
29 Sides Papadam
30 Sides Salad
31 Dessert Gulab Jamun
32 Dessert Fruit Custard
33 Dessert Semiya Payasam
34 Dessert Coconut Pudding

Industry/Entity Type

Restaurant

Requirements
Must have
• Title
• Easter Buffet - Extravagant Family Buffet

```html
<!DOCTYPE html>
<html lang="en">
<head>
<meta charset="utf-8">
<title>Pepper Meadow Indian Restaurant – Easter Dinner Buffet</title>
<link rel="stylesheet" href="https://fonts.googleapis.com/css2?family=Quicksand:wght@400;500;600;700&display=swap">
<style>
  :root {
    --gold: #f6c02a;
    --gold-soft: rgba(246, 192, 42, 0.35);
    --bg-center: #6f6a4e;
    --bg-edge: #2f2c1d;
  }
  * { margin: 0; padding: 0; box-sizing: border-box; }
  html, body { width: 795px; height: 1200px; overflow: hidden; }
  body {
    font-family: "Quicksand", sans-serif;
    color: var(--gold);
    background: radial-gradient(ellipse at 50% 50%, var(--bg-center) 0%, #4b4732 55%, var(--bg-edge) 100%);
    position: relative;
  }
  .poster-frame {
    position: absolute;
    inset: 34px;
    border: 3px solid var(--gold);
  }
  .corner-flourish {
    position: absolute;
    width: 110px;
    height: 110px;
    background: radial-gradient(circle at center, var(--gold-soft) 0%, rgba(246, 192, 42, 0.08) 60%, transparent 75%);
  }
  .corner-flourish.top-left { top: 14px; left: 14px; }
  .corner-flourish.top-right { top: 14px; right: 14px; }
  .corner-flourish.bottom-left { bottom: 14px; left: 14px; }
  .corner-flourish.bottom-right { bottom: 14px; right: 14px; }

  .line {
    position: absolute;
    left: 0;
    width: 100%;
    text-align: center;
    text-transform: uppercase;
    white-space: nowrap;
    transform: translateY(-50%);
  }
  .restaurant-name { font-weight: 700; font-size: 44px; letter-spacing: 0.5px; }
  .feature { font-weight: 400; font-size: 35px; }
  .price { font-weight: 600; font-size: 33px; }
  .availability { font-weight: 600; font-size: 35px; }

  .divider {
    position: absolute;
    left: 185px;
    width: 425px;
    height: 3px;
    background: var(--gold);
  }
</style>
</head>
<body>
  <div class="poster-frame"></div>
  <div class="corner-flourish top-left" role="img" aria-label="Gold ornamental corner flourish"></div>
  <div class="corner-flourish top-right" role="img" aria-label="Gold ornamental corner flourish"></div>
  <div class="corner-flourish bottom-left" role="img" aria-label="Gold ornamental corner flourish"></div>
  <div class="corner-flourish bottom-right" role="img" aria-label="Gold ornamental corner flourish"></div>

  <header>
    <h1 class="line restaurant-name" style="top:128px">Pepper Meadow</h1>
    <p class="line restaurant-name" style="top:208px">Indian Restaurant</p>
  </header>

  <div class="divider" style="top:312px"></div>

  <section class="menu-highlights">
    <p class="line feature" style="top:403px">35+ Items on the menu</p>
    <p class="line feature" style="top:485px">Sea food ,Goat , Lamb,</p>
    <p class="line feature" style="top:530px">Chicken varieties</p>
    <p class="line feature" style="top:615px">Plenty of options for</p>
    <p class="line feature" style="top:665px">Vegetarians and vegans</p>
  </section>

  <section class="pricing">
    <p class="line price" style="top:756px">Adult price $34.50</p>
    <p class="line price" style="top:803px">Kids under 12 eat at $21.</p>
    <p class="line price" style="top:850px">Kids under 2 free</p>
  </section>

  <div class="divider" style="top:913px"></div>

  <section class="opening-times">
    <p class="line availability" style="top:1000px">Available during all</p>
    <p class="line availability" style="top:1052px">Easter holidays</p>
    <p class="line availability" style="top:1104px">(5:30PM-9:30PM)</p>
  </section>
</body>
</html>
```